Book cover design for a book named BLOOM

Hello Designers,
The name of the book is BLOOM and it is about unexpected experiences individuals have which are beyond their control. Occurrences they are unable to overcome or get out of themselves without the help of God. After overcoming these situations they know only God could have done this for them, no one else could have. It is an adult Christian book. I would like you to be as creative as you can with the cover, using color, light, graphic designs, shapes, scale, lines etc. (you are the designers, I don't know how to do these things.) I would like to use the image created on a paperback, hardcover or e book. I tried to use an image from Pixmarble just to give you some idea of my thinking but you do not have to use these hands. The hands should look as if they are giving someone the word TESTIMONY not receiving it. Use of the words provided, the light rays, and some type of hands extended should not change, but how you use them is up to you. Use the words, light rays, and hands however you wish as long as they convey someone giving the word TESTIMONY. The word TESTIMONY should be proportional to the hand in size and should appear as if being held in the actual hand it should not be larger than the book name. It is a Christian book of testimonies. Also for your design samples you can use the name Marlene Quiller for the author. Thank you, please feel free to contact me if you have any questions. I am looking for the cover to be an attention grabber and give the reader something to really think about and remember visually when they see this cover. Thank you again.

Target Market(s)

anyone and christians

Requirements
Must have
• Use of the words provided, the light rays, and some type of hands extended should not change.
Nice to have
• be as creative as you can with the cover, using color, light, graphic designs, shapes, scale, lines etc. (you are the designers, I don't know how to do these things.)
Should not have
• It should not have fonts, colors, etc. that convey it is a child's book, fairytale, or fictional etc. It is a book of true stories that actually happened. It should not look exactly like my example, what I provided.

```html
<!DOCTYPE html>
<html lang="en">
<head>
<meta charset="UTF-8">
<title>Bloom — Book Cover</title>
<link rel="stylesheet" href="https://fonts.googleapis.com/css2?family=Dancing+Script:wght@700&family=Libre+Baskerville:ital,wght@0,400;0,700&display=swap">
<style>
  :root {
    --page: #ffffff;
    --night-deep: #0a1f5c;
    --night-mid: #12388c;
    --night-low: #1a62b8;
    --glow: #7fd8ff;
    --glow-soft: #d6f6ff;
    --hand-blue: #4fb8ee;
    --leaf: #4cb648;
    --ink-light: #ffffff;
    --testimony-cyan: #5fe6ff;
  }
  * { margin: 0; padding: 0; box-sizing: border-box; }
  html, body {
    width: 1200px;
    height: 1200px;
    overflow: hidden;
    background: var(--page);
  }
  .cover {
    position: absolute;
    left: 232px;
    top: 34px;
    width: 708px;
    height: 1134px;
    overflow: hidden;
    background: var(--night-deep);
  }
  .sky-photo {
    position: absolute;
    inset: 0;
    background:
      radial-gradient(ellipse 60% 30% at 50% 52%, rgba(40, 100, 200, 0.5), transparent 70%),
      linear-gradient(180deg, var(--night-deep) 0%, var(--night-mid) 50%, var(--night-low) 100%);
  }
  .light-rays {
    position: absolute;
    left: 0;
    bottom: 0;
    width: 100%;
    height: 480px;
    background: radial-gradient(ellipse 75% 60% at 65% 55%, rgba(150, 225, 255, 0.38), transparent 75%);
  }
  .tagline {
    position: absolute;
    top: 196px;
    left: 0;
    width: 100%;
    text-align: center;
    font-family: "Libre Baskerville", Georgia, serif;
    font-size: 25px;
    line-height: 27px;
    color: var(--ink-light);
    z-index: 3;
  }
  .tagline strong { font-weight: 700; }
  .title {
    position: absolute;
    top: 262px;
    left: 0;
    width: 100%;
    text-align: center;
    font-family: "Dancing Script", cursive;
    font-weight: 700;
    font-size: 260px;
    line-height: 1;
    color: var(--ink-light);
    text-shadow: 0 6px 14px rgba(0, 0, 30, 0.45);
    z-index: 3;
  }
  .laurel-area {
    position: absolute;
    left: 45px;
    top: 505px;
    width: 617px;
    height: 80px;
    border-radius: 50%;
    background: radial-gradient(ellipse at center, rgba(76, 182, 72, 0.6), rgba(76, 182, 72, 0) 70%);
    z-index: 2;
  }
  .promise {
    position: absolute;
    top: 683px;
    left: 0;
    width: 100%;
    text-align: center;
    font-family: "Libre Baskerville", Georgia, serif;
    font-size: 25px;
    line-height: 26px;
    color: var(--ink-light);
    text-transform: uppercase;
    z-index: 3;
  }
  .promise strong { font-weight: 700; }
  .giving-hand {
    position: absolute;
    left: 50px;
    top: 752px;
    width: 680px;
    height: 300px;
    border-radius: 18% 40% 45% 30% / 25% 45% 55% 45%;
    background:
      radial-gradient(ellipse 35% 35% at 55% 60%, var(--glow-soft), rgba(214, 246, 255, 0) 100%),
      linear-gradient(160deg, rgba(79, 184, 238, 0.85) 0%, rgba(127, 216, 255, 0.8) 55%, rgba(79, 184, 238, 0.55) 100%);
    filter: blur(3px);
    z-index: 1;
  }
  .held-word-stage {
    position: absolute;
    left: 45px;
    top: 818px;
    width: 617px;
    height: 110px;
    perspective: 420px;
    z-index: 2;
  }
  .held-word {
    display: block;
    text-align: center;
    font-family: "Libre Baskerville", Georgia, serif;
    font-style: normal;
    font-weight: 400;
    font-size: 92px;
    line-height: 110px;
    color: var(--testimony-cyan);
    transform: rotateX(34deg);
    transform-origin: 50% 100%;
    text-shadow: 0 0 8px rgba(191, 240, 255, 0.7);
    opacity: 0.9;
  }
</style>
</head>
<body>
  <main class="cover">
    <div class="sky-photo" role="img" aria-label="Starry night sky photograph in deep blues"></div>
    <div class="light-rays"></div>

    <p class="tagline">
      Before there will ever be a <strong>TESTIMONY</strong><br>
      there must always be an <strong>EXPERIENCE</strong>
    </p>

    <h1 class="title">Bloom</h1>
    <div class="laurel-area" role="img" aria-label="Green leafy vine ornament beneath the title"></div>

    <p class="promise">
      Out of the test I’ve given you a<br>
      <strong>Testimony</strong>
    </p>

    <div class="giving-hand" role="img" aria-label="Glowing blue open hand extended palm up, offering the word outward"></div>
    <div class="held-word-stage">
      <span class="held-word">TESTIMONY</span>
    </div>
  </main>
</body>
</html>
```